Men’s hair skin and beard line

I own a men’s salon in Texas and are beginning to expand its market into the men’s retail line and already have it being manufactured out of the UK. It’s paraben free, vegan, sulphate free. I need a better brand look for the packaging. This script font is a bit hard to read. I want it masculine yet clean lines. All colors even gold or silver are welcomed. Bottle choices are silver canisters, white or black.

Target Market(s)

Men

Industry/Entity Type

Men’s hair skin and beard industry. Retail centers, high end barbers, and gyms

Font styles to use
Other font styles liked:
• Montserrat ,helvetica neue, or lato font

Colors
0054AA
0677BA
7BADD7
CADEEF
E8F1F8
0094D4
00A9DD
6FCCEA
C7EBF8
E9F6FB
00AB8E
00BBA5
67D7C9
C6EFE9
E9F9F6

Requirements
Must have
• Logo and name
Nice to have
• I’m open to all.
Should not have
• Not feminine

```html
<!DOCTYPE html>
<html lang="en">
<head>
<meta charset="utf-8">
<title>Vantore Men's Fine Grooming – Label Set</title>
<link rel="stylesheet" href="https://fonts.googleapis.com/css2?family=Montserrat:wght@400;500;700;800&display=swap">
<style>
  :root {
    --canvas: #ffffff;
    --label-black: #030303;
    --text-white: #ffffff;
    --brand-grey: #3d3d3d;
    --mark-grey: #8c8c8c;
    --silver-dark: #5a5a5a;
    --silver-mid: #a9a9a9;
    --silver-light: #ececec;
  }
  * { box-sizing: border-box; margin: 0; padding: 0; }
  html, body {
    width: 1200px; height: 1200px; overflow: hidden;
    background: var(--canvas);
    font-family: "Montserrat", sans-serif;
  }
  .sheet { position: relative; width: 1200px; height: 1200px; }

  .label {
    position: absolute;
    background: var(--label-black);
    color: var(--text-white);
    overflow: hidden;
  }
  .label > * { position: absolute; left: 0; right: 0; text-align: center; }

  .silver-band {
    height: 9px;
    background: linear-gradient(90deg,
      var(--silver-dark) 0%, var(--silver-mid) 12%, var(--silver-light) 30%,
      var(--silver-mid) 50%, var(--silver-light) 72%, var(--silver-mid) 88%,
      var(--silver-dark) 100%);
  }

  .brand-square {
    margin: 0 auto;
    background: var(--mark-grey);
  }
  .brand-name {
    font-weight: 800;
    color: var(--brand-grey);
    letter-spacing: 0.01em;
    line-height: 1;
  }
  .brand-tagline {
    font-weight: 700;
    color: var(--brand-grey);
    letter-spacing: 0.08em;
    line-height: 1;
    white-space: nowrap;
  }

  .product-title {
    font-weight: 400;
    line-height: 1;
    letter-spacing: 0.02em;
    text-transform: uppercase;
  }
  .product-subtitle {
    font-weight: 700;
    letter-spacing: 0.12em;
    text-transform: uppercase;
    line-height: 1;
  }
  .product-copy {
    font-size: 9.2px;
    line-height: 1.25;
    text-align: justify;
    text-align-last: center;
  }
  .product-volume { font-weight: 700; line-height: 1; }

  /* Beard oil */
  .label--beard { left: 159px; top: 367px; width: 246px; height: 454px; }
  .label--beard .band-top { top: 11px; }
  .label--beard .band-bottom { bottom: 14px; }
  .label--beard .brand-square { top: 64px; width: 56px; height: 56px; left: 95px; right: auto; }
  .label--beard .brand-name { top: 127px; font-size: 30px; }
  .label--beard .brand-tagline { top: 156px; font-size: 8.5px; }
  .label--beard .product-title { top: 205px; font-size: 44px; line-height: 1.1; }
  .label--beard .product-subtitle { top: 327px; font-size: 11.5px; }
  .label--beard .product-volume { top: 411px; font-size: 10px; }

  /* Tall bottle labels */
  .label--tall { top: 105px; width: 368px; height: 716px; }
  .label--facial { left: 422px; }
  .label--clearing { left: 806px; }
  .label--tall .band-top { top: 19px; }
  .label--tall .band-bottom { bottom: 13px; }
  .label--tall .brand-square { top: 80px; width: 84px; height: 84px; left: 142px; right: auto; }
  .label--tall .brand-name { top: 178px; font-size: 49px; }
  .label--tall .brand-tagline { top: 226px; font-size: 14px; }
  .label--tall .title-line-1 { top: 312px; font-size: 83px; }
  .label--tall .title-line-2 { top: 388px; font-size: 52px; }
  .label--clearing .title-line-1 { font-size: 55px; top: 318px; }
  .label--clearing .title-line-2 { font-size: 80px; top: 372px; }
  .label--tall .product-subtitle { top: 503px; font-size: 15.5px; }
  .label--tall .product-copy { top: 545px; left: 43px; right: 33px; }
  .label--tall .product-volume { top: 669px; font-size: 16px; }

  /* Shaving cream tube band */
  .label--shave { left: 214px; top: 869px; width: 785px; height: 160px; }
  .label--shave .band-bottom { bottom: 14px; }
  .label--shave .product-title { top: 44px; left: 23px; right: auto; text-align: left; font-size: 46px; }
  .label--shave .product-subtitle { top: 92px; left: 25px; right: auto; text-align: left; font-size: 14.5px; }
  .label--shave .shave-brand { left: 570px; right: auto; width: 170px; top: 0; bottom: 0; }
  .label--shave .shave-brand > * { position: absolute; left: 0; right: 0; text-align: center; }
  .label--shave .brand-square { top: 18px; width: 50px; height: 50px; left: 60px; right: auto; }
  .label--shave .brand-name { top: 80px; font-size: 30px; }
  .label--shave .brand-tagline { top: 110px; font-size: 8.5px; }
</style>
</head>
<body>
<main class="sheet">

  <section class="label label--beard" aria-label="Beard oil label">
    <div class="silver-band band-top"></div>
    <div class="brand-square"></div>
    <p class="brand-name">VANTORE</p>
    <p class="brand-tagline">— MEN’S FINE GROOMING —</p>
    <h2 class="product-title">Beard<br>Oil</h2>
    <p class="product-subtitle">Famous Fragrance</p>
    <p class="product-volume">30ml/1.0floz</p>
    <div class="silver-band band-bottom"></div>
  </section>

  <section class="label label--tall label--facial" aria-label="Facial cleanser label">
    <div class="silver-band band-top"></div>
    <div class="brand-square"></div>
    <p class="brand-name">VANTORE</p>
    <p class="brand-tagline">— MEN’S FINE GROOMING —</p>
    <h2 class="product-title title-line-1">Facial</h2>
    <h2 class="product-title title-line-2">Cleanser</h2>
    <p class="product-subtitle">Post Wash Facial Cleanser</p>
    <p class="product-copy">Lorem ipsum dolor sit amet, consectetuer adipiscing elit, sed diam nonummy nibh euismod tincidunt ut laoreet dolore magna aliquam erat volutpat. Ut wisi enim ad minim veniam, quis nostrud exerci tation ullamcorper suscipit lobortis nisl ut aliquip ex ea commodo consequat. Duis autem vel eum iriure dolor in hendrerit in vulputate velit esse mo</p>
    <p class="product-volume">100ml/3.4floz</p>
    <div class="silver-band band-bottom"></div>
  </section>

  <section class="label label--tall label--clearing" aria-label="Clearing gel label">
    <div class="silver-band band-top"></div>
    <div class="brand-square"></div>
    <p class="brand-name">VANTORE</p>
    <p class="brand-tagline">— MEN’S FINE GROOMING —</p>
    <h2 class="product-title title-line-1">Clearing</h2>
    <h2 class="product-title title-line-2">Gel</h2>
    <p class="product-subtitle">Clearing Gel</p>
    <p class="product-copy">Lorem ipsum dolor sit amet, consectetuer adipiscing elit, sed diam nonummy nibh euismod tincidunt ut laoreet dolore magna aliquam erat volutpat. Ut wisi enim ad minim veniam, quis nostrud exerci tation ullamcorper suscipit lobortis nisl ut aliquip ex ea commodo consequat. Duis autem vel eum iriure dolor in hendrerit in vulputate velit esse mo</p>
    <p class="product-volume">100ml/3.4floz</p>
    <div class="silver-band band-bottom"></div>
  </section>

  <section class="label label--shave" aria-label="Shaving cream label">
    <h2 class="product-title">Shaving Cream</h2>
    <p class="product-subtitle">Luxurious Traditional Shave</p>
    <div class="shave-brand">
      <div class="brand-square"></div>
      <p class="brand-name">VANTORE</p>
      <p class="brand-tagline">— MEN’S FINE GROOMING —</p>
    </div>
    <div class="silver-band band-bottom"></div>
  </section>

</main>
</body>
</html>
```